TEK Logistics - Banner 2.5' x 8' for 20+ locations

Need a banner designed that will pop. This banner will be displayed at over 20 of our transportation facilities. Goal is for the banner to grab the attention of employees, contractors and clients and help reinforce our mission and core values. Designed needs to include TEK Logo, our core values and mission statement. Red and Black are the main company colors and we need to stay within that theme and color pallet. Attached is a previous version that was too basic and boring. Willing to consider a design that excludes the mission statement.

Gathering more feedback

```html
<!DOCTYPE html>
<html lang="en">
<head>
<meta charset="utf-8">
<title>TEK Logistics Banner</title>
<link rel="stylesheet" href="https://fonts.googleapis.com/css2?family=Saira:wght@600&family=Montserrat:wght@500&display=swap">
<style>
  :root {
    --backdrop: #bebebe;
    --brand-red: #d22627;
    --ink: #2b2825;
    --paper: #ffffff;
    --chevron: #f1f1f1;
  }
  * { margin: 0; padding: 0; box-sizing: border-box; }
  html, body {
    width: 1200px;
    height: 970px;
    overflow: hidden;
    background: var(--backdrop);
  }
  .banner {
    position: absolute;
    left: 43px;
    top: 322px;
    width: 1114px;
    height: 348px;
    background: var(--brand-red);
    overflow: hidden;
  }
  .banner__shapes {
    position: absolute;
    inset: 0;
  }
  .brand-name {
    position: absolute;
    left: 82px;
    top: 118px;
    width: 260px;
    color: var(--brand-red);
    font-family: "Saira", sans-serif;
    font-weight: 600;
    text-align: center;
    line-height: 1;
  }
  .brand-name__main {
    display: block;
    font-size: 78px;
    letter-spacing: 3px;
  }
  .brand-name__sub {
    display: block;
    font-size: 27px;
    letter-spacing: 7px;
    margin-top: 2px;
  }
  .core-values {
    position: absolute;
    right: 56px;
    top: 44px;
    list-style: none;
    font-family: "Saira", sans-serif;
    font-weight: 600;
    font-size: 23px;
    letter-spacing: 0.3px;
    text-align: right;
  }
  .core-values__row {
    height: 37.7px;
    line-height: 32px;
    white-space: nowrap;
  }
  .value { display: inline-block; }
  .value + .value { margin-left: 32px; }
  .value__chevron {
    width: 14px;
    height: 16px;
    vertical-align: -1px;
    margin-right: 6px;
  }
  .tone-light { color: var(--paper); }
  .tone-dark { color: var(--ink); }
  .divider {
    position: absolute;
    left: 583px;
    right: 0;
    top: 252px;
    height: 1.5px;
    background: var(--paper);
  }
  .mission {
    position: absolute;
    right: 56px;
    top: 257px;
    color: var(--paper);
    font-family: "Montserrat", sans-serif;
    font-weight: 500;
    font-size: 14.6px;
    line-height: 18.7px;
    text-align: right;
    white-space: nowrap;
  }
  .mission__line { display: block; }
</style>
</head>
<body>
  <div class="banner">
    <svg class="banner__shapes" width="1114" height="348" viewBox="0 0 1114 348">
      <defs>
        <linearGradient id="accent-fill" x1="0" y1="0" x2="1" y2="0">
          <stop offset="0" stop-color="#ffffff"/>
          <stop offset="1" stop-color="#2b2825"/>
        </linearGradient>
      </defs>
      <polygon fill="var(--paper)" points="0,0 270,0 380,348 0,348" aria-hidden="true"/>
      <polygon fill="url(#accent-fill)" points="330,0 420,0 540,348 450,348" role="img" aria-label="Decorative stripe accent in white, red and black"/>
    </svg>

    <div class="brand-name">
      <span class="brand-name__main">TEK</span>
      <span class="brand-name__sub">LOGISTICS</span>
    </div>

    <ul class="core-values">
      <li class="core-values__row">
        <span class="value"><svg class="value__chevron" viewBox="0 0 14 16"><path fill="var(--chevron)" d="M0 0 H6 L14 8 L6 16 H0 L6 8 Z"/></svg><span class="tone-light">DO THE RIGHT THINGS</span> <span class="tone-dark">FOR THE RIGHT REASONS</span></span>
      </li>
      <li class="core-values__row">
        <span class="value"><svg class="value__chevron" viewBox="0 0 14 16"><path fill="var(--chevron)" d="M0 0 H6 L14 8 L6 16 H0 L6 8 Z"/></svg> <span class="tone-dark">PURSUE</span> <span class="tone-light">GROWTH AND DEVELOPMENT</span></span>
      </li>
      <li class="core-values__row">
        <span class="value"><svg class="value__chevron" viewBox="0 0 14 16"><path fill="var(--chevron)" d="M0 0 H6 L14 8 L6 16 H0 L6 8 Z"/></svg> <span class="tone-light">BUILD A POSITIVE</span> <span class="tone-dark">TEAM ATMOSPHERE</span></span>
      </li>
      <li class="core-values__row">
        <span class="value"><svg class="value__chevron" viewBox="0 0 14 16"><path fill="var(--chevron)" d="M0 0 H6 L14 8 L6 16 H0 L6 8 Z"/></svg><span class="tone-light">DELIVER WOW</span> <span class="tone-dark">THROUGH SERVICE</span></span>
      </li>
      <li class="core-values__row">
        <span class="value"><svg class="value__chevron" viewBox="0 0 14 16"><path fill="var(--chevron)" d="M0 0 H6 L14 8 L6 16 H0 L6 8 Z"/></svg><span class="tone-light">DO EVERYTHING</span> <span class="tone-dark">SAFELY</span></span><span class="value"><svg class="value__chevron" viewBox="0 0 14 16"><path fill="var(--chevron)" d="M0 0 H6 L14 8 L6 16 H0 L6 8 Z"/></svg> <span class="tone-dark">HAVE FUN</span></span>
      </li>
    </ul>

    <div class="divider"></div>

    <p class="mission">
      <span class="mission__line">Provide the best customer experience while creating an</span>
      <span class="mission__line">environment of growth and opportunity for our customers,</span>
      <span class="mission__line">employees, and service providers.</span>
    </p>
  </div>
</body>
</html>
```